Atendimento nota 11, sem contar a agilidade das pessoas, nos apresentaram diversos modelos e formas de logo. Com certeza iremos indica-lo para outras pessoas.

```html
<!DOCTYPE html>
<html lang="pt-BR">
<head>
<meta charset="UTF-8">
<title>Vértice Imóveis — Papel Timbrado</title>
<link rel="stylesheet" href="https://fonts.googleapis.com/css2?family=Montserrat:wght@300;400&display=swap">
<style>
  :root {
    --backdrop: #e6e6e6;
    --paper: #ffffff;
    --ink: #2a2a2a;
    --ink-soft: #3a3a3a;
    --gold: #b89a4e;
    --rule: #111111;
  }
  * { margin: 0; padding: 0; box-sizing: border-box; }
  html, body {
    width: 1200px;
    height: 1200px;
    overflow: hidden;
    background: var(--backdrop);
    font-family: "Montserrat", Arial, sans-serif;
  }
  .letterhead {
    position: absolute;
    left: 252px;
    top: 36px;
    width: 696px;
    height: 1128px;
    background: var(--paper);
    box-shadow: 0 2px 10px rgba(0, 0, 0, 0.12);
  }
  .brand {
    position: absolute;
    top: 74px;
    left: 0;
    right: 0;
    display: flex;
    flex-direction: column;
    align-items: center;
    gap: 14px;
  }
  .brand-square {
    width: 30px;
    height: 30px;
    background: var(--gold);
  }
  .brand-name {
    font-weight: 300;
    font-size: 30px;
    letter-spacing: 3px;
    color: var(--ink);
    text-transform: uppercase;
  }
  .contact {
    position: absolute;
    left: 0;
    right: 0;
    top: 1015px;
    text-align: center;
    font-size: 11px;
    line-height: 15px;
    color: var(--ink-soft);
  }
  .footer-rule {
    position: absolute;
    left: 14px;
    right: 14px;
    top: 1058px;
    height: 4px;
    background: var(--rule);
  }
</style>
</head>
<body>
  <main class="letterhead">
    <header class="brand">
      <div class="brand-square"></div>
      <div class="brand-name">Vértice Imóveis</div>
    </header>
    <footer>
      <p class="contact">
        Rua 318, nº 45, Sala 04 Porto Claro - Centro - SC<br>
        CEP: 88310-000 - (47) 3000-4815
      </p>
      <div class="footer-rule"></div>
    </footer>
  </main>
</body>
</html>
```